Renewed electronic office supplies

I need a landing page design for a B2B business that will sell refurbished and renewed electronic devices such as smartphones, laptops, tablets and other gadgets. We want to become suppliers of these devices to companies that need computers and other devices for their employees. The point of our business is that they can get a great device that is in very good contrition instead of buying brand new. Companies will be able to save 50-60% on these renewed devices. Not only that we will also buy the companies old devices which they no longe needs and renew them and give them new life so we can resell it.

Our services will be:

- sale of renewed devices with lifetime warranty

- purchase of old devices

- swap solution: meaning client buy from us and sell at the same time so we deduct the amount sale of their old devices into their purchase.

Some useful information:

- company name and logo are still pending

- we aim to provide all business with top quality of renewed and environmentally friendly electronics, while maintaining a minimal impact on the natural environment.

I have attached a word document with some additional info that might be useful

Looking forward to seeing all your great designs!

P.s. Please feel free to make designs that are not based on my documents also, we need different layouts and designs. as for now I see many of the designs are more or less the same. we need more variation on design
Updates

Target Market(s)

Medium to large Businesses

Industry/Entity Type

Technology Equipment

Requirements
Must have
• we need more designs to be submitted , 50 designs minimum

```html
<!DOCTYPE html>
<html lang="en">
<head>
<meta charset="utf-8">
<title>Renewed Electronic Office Supplies</title>
<link href="https://fonts.googleapis.com/css2?family=Poppins:wght@400;500;600;700&family=Roboto:wght@400;500&display=swap" rel="stylesheet">
<style>
:root{
  --navy:#103566;
  --green:#2fcf78;
  --purple:#6a4fc6;
  --purple-light:#b9a9e8;
  --ink:#1d1d2b;
  --muted:#6b6b78;
  --grey-bg:#f2f2f3;
  --footer:#2b2b2e;
  --white:#ffffff;
}
*{box-sizing:border-box;margin:0;padding:0}
html,body{width:1200px;height:4792px;overflow:hidden}
body{font-family:"Poppins",sans-serif;color:var(--ink);background:var(--white);position:relative}
.abs{position:absolute}
.btn{position:absolute;display:flex;align-items:center;justify-content:center;gap:8px;border-radius:30px;font-weight:600;color:var(--white);font-size:15px}
.btn-green{background:var(--green)}
.btn-purple{background:var(--purple);font-weight:500;font-size:13px}
.btn .ring{width:17px;height:17px;border:1.6px solid #fff;border-radius:50%;display:flex;align-items:center;justify-content:center}

/* hero */
.hero-bg{position:absolute;left:0;top:0;width:1200px;height:800px}
.logo{position:absolute;font-weight:700;font-size:32px;color:var(--white);letter-spacing:1px}
.nav a{position:absolute;top:36px;color:var(--white);font-size:14px;font-weight:500;text-decoration:none}
.hero-title{position:absolute;left:162px;top:206px;color:var(--white);font-weight:700;line-height:1}
.hero-title .big{font-size:70px;display:block}
.hero-title .sub{font-size:40px;display:block;margin-top:12px;line-height:1.2}
.hero-text{position:absolute;left:162px;top:396px;width:450px;color:var(--white);font-size:13.5px;line-height:24px}
.phone-ph{position:absolute;border-radius:34px;border:6px solid #222}

/* categories */
.cat{position:absolute;width:207px;height:214px;border-radius:4px;background:linear-gradient(160deg,#8c7bc9,#5a3fae);box-shadow:0 10px 22px rgba(60,40,120,.25);color:#fff;text-align:center}
.cat span{position:absolute;left:0;right:0;top:140px;font-size:21px;font-weight:600}
.cat i{position:absolute;left:50%;top:182px;margin-left:-10px;width:20px;height:20px;border:1.6px solid #fff;border-radius:50%}
.arrow{position:absolute;width:36px;height:36px;border:2px solid var(--green);border-radius:50%}

/* who */
.who{position:absolute;left:0;top:1190px;width:1200px;height:592px;background:var(--grey-bg)}
.h2{font-weight:700;font-size:38px;color:var(--ink)}
.feature-icon{position:absolute;width:58px;height:58px;border-radius:50%;display:flex;align-items:center;justify-content:center}
.feature h4{font-size:17px;font-weight:600;margin-bottom:6px}
.feature p,.who-text{font-family:"Roboto",sans-serif;font-size:12.5px;line-height:20px;color:var(--muted)}

/* services */
.svc{position:absolute;top:1946px;width:236px;height:240px;background:#f4f4f5;border:1px solid #e2e2e6;text-align:center}
.svc svg{margin-top:34px}
.svc h5{font-size:14px;font-weight:500;margin-top:14px}
.svc p{font-family:"Roboto",sans-serif;font-size:11.5px;line-height:18px;color:var(--muted);margin:8px auto 0;width:190px}
.svc.active{background:var(--purple);border-color:var(--purple);color:#fff}
.svc.active p{color:#fff}

/* product */
.prod h3{font-size:34px;font-weight:600}
.prod .lead{font-family:"Roboto",sans-serif;font-size:15px;line-height:21px;color:var(--muted);width:330px;margin-top:8px}
.prod .prices{display:flex;gap:0;margin-top:22px;font-size:15px;font-weight:600}
.prod .prices .ours{color:var(--purple);width:186px}
.prod .prices .new{color:#555}
.prod .saved{font-size:15px;font-weight:600;color:#555;margin-top:16px}

/* testimonials */
.quote{position:absolute;top:3646px;width:450px;height:200px;border-radius:4px;padding:30px 32px;font-family:"Roboto",sans-serif;font-size:13px;line-height:23px;color:#777;background:#fff}
.quote.dim{background:#c3b6ec;color:#8f7fcc}
.quote .who-line{display:flex;align-items:center;gap:18px;margin-top:26px}
.quote .avatar{width:56px;height:56px;background:#b8b8c0}
.quote .name{font-size:15px;color:#333}
.quote.dim .name{color:#7a68c4}
.quote .role{font-size:13px}

/* contact */
.contact-line{position:absolute;left:219px;display:flex;align-items:center;gap:10px;font-family:"Roboto",sans-serif;font-size:14px;color:#444}

/* footer */
.footer{position:absolute;left:0;top:4325px;width:1200px;height:467px;background:var(--footer);color:#fff}
.fcol{position:absolute;top:169px;font-size:13px;line-height:33px}
.fcol h6{font-size:13px;font-weight:600;margin-bottom:0}
.fcol a{display:block;color:#fff;text-decoration:underline;font-size:12px;line-height:25px}
.fcol.plain a{text-decoration:none;font-weight:500;font-size:13px;line-height:33px}
.social{position:absolute;top:4662px;width:32px;height:32px;border:1.5px solid #fff;border-radius:50%}
</style>
</head>
<body>

<!-- HERO -->
<svg class="hero-bg" viewBox="0 0 1200 800" aria-hidden="true">
  <polygon points="0,0 1200,0 1200,255 0,785" fill="var(--navy)"/>
  <polygon points="1200,255 1200,690 610,516" fill="var(--green)"/>
</svg>
<div class="logo" style="left:162px;top:28px">LOGO</div>
<nav class="nav">
  <a style="left:516px">Home</a>
  <a style="left:600px">Services</a>
  <a style="left:704px">News</a>
  <a style="left:785px">About Us</a>
</nav>
<div class="btn btn-green" style="left:893px;top:24px;width:146px;height:43px;font-weight:500;font-size:14px">Contact us</div>

<h1 class="hero-title"><span class="big">REUSABLE</span><span class="sub">ELECTRONIC OFFICE<br>SUPPLIES</span></h1>
<p class="hero-text">we aim to provide all business with top quality of reused and environmentally friendly electronics, while maintaining a minimal impact on the natural environment.</p>
<div class="btn btn-green" style="left:162px;top:497px;width:170px;height:41px">SHOP NOW <span class="ring"><svg width="7" height="9" viewBox="0 0 7 9"><path d="M1 1l4 3.5L1 8" stroke="#fff" stroke-width="1.6" fill="none"/></svg></span></div>

<div class="phone-ph" role="img" aria-label="Smartphone showing a travel booking app" style="left:640px;top:150px;width:200px;height:420px;transform:rotate(-22deg);background:linear-gradient(180deg,#2a88b8,#e9eef4 55%,#f7f7f9)"></div>
<div class="phone-ph" role="img" aria-label="Smartphone showing a map route app" style="left:890px;top:265px;width:180px;height:420px;transform:rotate(10deg);background:linear-gradient(180deg,#4a4a52,#2b3d2c 60%,#f06a63)"></div>

<!-- CATEGORIES -->
<div class="arrow" style="left:107px;top:921px"><svg width="32" height="32" viewBox="0 0 32 32"><path d="M19 9l-7 7 7 7" stroke="var(--green)" stroke-width="2.4" fill="none"/></svg></div>
<div class="cat" role="img" aria-label="Photo of a hand holding a smartphone" style="left:164px;top:831px"><span>Smartphones</span><i></i></div>
<div class="cat" role="img" aria-label="Photo of a laptop on a desk" style="left:385px;top:815px"><span>Laptops</span><i></i></div>
<div class="cat" role="img" aria-label="Photo of a tablet" style="left:608px;top:831px"><span>Tablets</span><i></i></div>
<div class="cat" role="img" aria-label="Photo of gadgets on a desk" style="left:830px;top:831px"><span>Gadgets</span><i></i></div>
<div class="arrow" style="left:1056px;top:921px"><svg width="32" height="32" viewBox="0 0 32 32"><path d="M13 9l7 7-7 7" stroke="var(--green)" stroke-width="2.4" fill="none"/></svg></div>

<!-- WHO WE ARE -->
<svg class="abs" style="left:0;top:1150px" width="1200" height="80" viewBox="0 0 1200 80" aria-hidden="true">
  <path d="M0 72 C 150 62 330 48 560 30 C 780 12 980 8 1200 28 L1200 80 L0 80 Z" fill="var(--grey-bg)"/>
  <path d="M80 80 C 260 60 400 50 560 36 C 760 18 960 10 1200 32" stroke="var(--purple)" stroke-width="5" fill="none"/>
</svg>
<div class="who"></div>
<h2 class="h2 abs" style="left:162px;top:1290px">WHO WE ARE</h2>
<div class="abs" style="left:162px;top:1347px;font-size:15px;font-weight:600;color:var(--purple)">A smarter circular solution for electronic supplies</div>
<p class="who-text abs" style="left:162px;top:1376px;width:480px">Billions of electronics are being made, sold, and disposed of every year a cycle that drives short-term profits for electronics manufacturers, but at too high a cost for the planet we all share. With our experience in the recycling market we can put an end to this cycle and offer a circular solution that is both affordable and environmentally friendly.</p>

<div class="feature-icon" style="left:161px;top:1499px;background:var(--purple)"><svg width="34" height="34" viewBox="0 0 34 34"><circle cx="17" cy="17" r="14" stroke="#fff" stroke-width="2" fill="none"/><path d="M10 17l5 5 9-10" stroke="#fff" stroke-width="2.2" fill="none"/></svg></div>
<div class="feature abs" style="left:238px;top:1502px;width:410px"><h4>Buy reusable IT</h4><p>We specialize in refurbished electronic devices with top quality for affordable prices. All our products have undergone a detailed testing and reconditioning program by expert technicians.</p></div>
<div class="feature-icon" style="left:161px;top:1608px;background:var(--green)"><svg width="34" height="34" viewBox="0 0 34 34"><circle cx="17" cy="17" r="14" stroke="#fff" stroke-width="2" fill="none"/><path d="M10 17l5 5 9-10" stroke="#fff" stroke-width="2.2" fill="none"/></svg></div>
<div class="feature abs" style="left:238px;top:1611px;width:410px"><h4>Sell your IT Safely</h4><p>We can also buy your used electronics and make sure they get reused and give them a new life. By selling your used devices that you no longer have use for you can help us create carbon savings.</p></div>

<div class="phone-ph" role="img" aria-label="Smartphone showing a lock screen with purple wallpaper" style="left:705px;top:1330px;width:170px;height:350px;transform:rotate(-9deg);background:linear-gradient(170deg,#3e3a9a,#6a4fd8 50%,#2a2470)"></div>
<div class="phone-ph" role="img" aria-label="Smartphone showing a purple mockup screen" style="left:885px;top:1320px;width:145px;height:300px;transform:rotate(9deg);background:linear-gradient(170deg,#4e45b0,#7c60e0 50%,#30286e)"></div>

<!-- SERVICES -->
<h2 class="h2 abs" style="left:0;width:1200px;text-align:center;top:1845px">OUR SERVICES</h2>
<div class="abs" style="left:556px;top:1896px;width:88px;height:3px;background:var(--purple)"></div>
<div class="abs" style="left:0;width:1200px;text-align:center;top:1906px;font-family:Roboto,sans-serif;font-size:15px;color:var(--muted)">A smarter circular solution for electronic supplies</div>

<div class="svc" style="left:106px">
  <svg width="84" height="74" viewBox="0 0 84 74" fill="none" stroke="#3a6fd0" stroke-width="2.4"><rect x="14" y="6" width="48" height="34" rx="3"/><path d="M8 46h60"/><rect x="4" y="28" width="18" height="34" rx="3"/><rect x="54" y="30" width="22" height="36" rx="3"/><circle cx="38" cy="22" r="7" stroke="var(--green)"/></svg>
  <h5>Sale Renewed devices</h5><p>Lorem Ipsum has been the industry's standard dummy text ever since the 1500s</p>
</div>
<div class="svc active" style="left:357px">
  <svg width="84" height="74" viewBox="0 0 84 74" fill="none" stroke="#fff" stroke-width="2.4"><rect x="12" y="18" width="60" height="38" rx="3"/><path d="M4 62h76"/><circle cx="48" cy="16" r="12" fill="var(--green)" stroke="none"/><path d="M48 8v16M52 11h-6a2.5 2.5 0 000 5h4a2.5 2.5 0 010 5h-6" stroke="#fff" stroke-width="2"/></svg>
  <h5>Purchase of old devices</h5><p>Lorem Ipsum has been the industry's standard dummy text ever since the 1500s</p>
</div>
<div class="svc" style="left:608px">
  <svg width="84" height="74" viewBox="0 0 84 74" fill="none" stroke-width="6"><path d="M24 42a20 20 0 0132-20" stroke="#3a6fd0"/><path d="M60 32a20 20 0 01-32 20" stroke="#6a4fc6"/><path d="M52 14l8 8-10 4" stroke="#3a6fd0" stroke-width="5"/><path d="M32 60l-8-8 10-4" stroke="#6a4fc6" stroke-width="5"/></svg>
  <h5>Swap Solution</h5><p>Lorem Ipsum has been the industry's standard dummy text ever since the 1500s</p>
</div>
<div class="svc" style="left:858px">
  <svg width="84" height="74" viewBox="0 0 84 74" fill="none" stroke="#3a6fd0" stroke-width="2.4"><circle cx="46" cy="36" r="30"/><ellipse cx="46" cy="36" rx="13" ry="30"/><path d="M16 36h60M20 21h52M20 51h52"/><path d="M10 62c6-18 20-24 30-22-4 14-16 24-30 22z" fill="var(--green)" stroke="none"/></svg>
  <h5>All businesses</h5><p>Lorem Ipsum has been the industry's standard dummy text ever since the 1500s</p>
</div>

<!-- PROMO BANNER -->
<div class="abs" role="img" aria-label="Photo of a workspace with a laptop and cup in purple tint" style="left:0;top:2288px;width:1200px;height:359px;background:linear-gradient(100deg,#5b4ab8,#6e58cc 45%,#5a45b4)"></div>
<div class="abs" style="left:300px;top:2384px;color:#fff;font-size:84px;font-weight:700;line-height:1">60%</div>
<div class="abs" style="left:488px;top:2366px;color:#fff;font-size:44px;font-weight:400;line-height:1.2">Save up to</div>
<div class="abs" style="left:489px;top:2427px;color:#fff;font-size:37px;font-weight:400;line-height:1.2">on our renewed devices</div>
<div class="btn btn-green" style="left:514px;top:2511px;width:171px;height:43px">SHOP NOW <span class="ring"><svg width="7" height="9" viewBox="0 0 7 9"><path d="M1 1l4 3.5L1 8" stroke="#fff" stroke-width="1.6" fill="none"/></svg></span></div>

<!-- PRODUCT 1 -->
<div class="prod abs" style="left:182px;top:2763px">
  <h3>NOVABOOK 5470</h3>
  <p class="lead">Price comparison between buying new or buying from us</p>
  <div class="prices"><span class="ours">Our price: 590$</span><span class="new">New price: 1390$</span></div>
  <div class="saved">Total saved: 60%</div>
</div>
<div class="btn btn-purple" style="left:186px;top:2957px;width:128px;height:32px">SHOP NOW</div>
<svg class="abs" style="left:600px;top:2706px" width="420" height="326" viewBox="0 0 420 326" aria-hidden="true">
  <path d="M80 90 C 120 10 250 -10 330 40 C 410 90 420 220 360 280 C 290 340 140 330 80 270 C 30 220 40 150 80 90Z" fill="#a9c3f0"/>
  <path d="M170 60 C 240 30 330 60 360 130 C 380 200 330 270 250 280 C 170 290 120 230 130 160 C 135 110 150 70 170 60Z" fill="#7fa6ea" opacity=".7"/>
</svg>
<div class="abs" role="img" aria-label="Photo of a renewed laptop" style="left:600px;top:2760px;width:340px;height:250px;border-radius:6px;background:linear-gradient(160deg,#3b4a5e,#1d2530 60%,#0f1318);transform:skewX(-6deg)"></div>
<div class="abs" style="left:24px;top:3078px;width:1176px;height:1px;background:#e2e2e6"></div>

<!-- PRODUCT 2 -->
<svg class="abs" style="left:279px;top:3140px" width="300" height="264" viewBox="0 0 300 264" aria-hidden="true">
  <path d="M40 110 C 60 40 150 10 220 40 C 290 70 300 170 250 220 C 200 270 90 260 50 210 C 25 180 30 140 40 110Z" fill="#a9c3f0"/>
  <path d="M110 70 C 170 50 240 90 240 150 C 240 210 180 240 130 220 C 90 205 80 160 90 120 C 95 95 100 80 110 70Z" fill="#7fa6ea" opacity=".7"/>
</svg>
<div class="abs" role="img" aria-label="Photo of a renewed smartphone, back and front" style="left:350px;top:3125px;width:160px;height:278px;border-radius:22px;background:linear-gradient(110deg,#1c1c1e,#3a3a3d 45%,#2f5a46 60%,#a24d3a)"></div>
<div class="prod abs" style="left:711px;top:3174px">
  <h3>ORBIT X 256 GB</h3>
  <p class="lead">Price comparison between buying new or buying from us</p>
  <div class="prices"><span class="ours">Our price: 550$</span><span class="new">New price: 790$</span></div>
  <div class="saved">Total saved: 30%</div>
</div>
<div class="btn btn-purple" style="left:713px;top:3368px;width:129px;height:32px">SHOP NOW</div>

<!-- TESTIMONIALS -->
<svg class="abs" style="left:0;top:3460px" width="1200" height="480" viewBox="0 0 1200 480" aria-hidden="true">
  <polygon points="0,38 1200,12 1200,30 0,58" fill="var(--purple-light)"/>
  <polygon points="0,52 1200,24 1200,479 0,479" fill="var(--purple)"/>
</svg>
<h2 class="abs" style="left:0;width:1200px;text-align:center;top:3573px;color:#fff;font-size:30px;font-weight:700">TESTIMONI ALS</h2>
<div class="quote dim" style="left:-98px">"Sed ut perspiciatis unde omnis iste natus error sit voluptatem accusan tium doloremque laudantium, totam rem aperiam, eaque ipsa quae."<div class="who-line"><div class="avatar" style="background:#a99fd6"></div><div><div class="name">John Doe</div><div class="role">CEO, Company</div></div></div></div>
<div class="quote" style="left:374px">"Sed ut perspiciatis unde omnis iste natus error sit voluptatem accusan tium doloremque laudantium, totam rem aperiam, eaque ipsa quae."<div class="who-line"><div class="avatar" role="img" aria-label="Customer portrait"></div><div><div class="name">John Doe</div><div class="role">CEO, Company</div></div></div></div>
<div class="quote dim" style="left:850px">"Sed ut perspiciatis unde omnis iste natus error sit voluptatem accusan tium doloremque laudantium, totam rem aperiam, eaque ipsa quae."<div class="who-line"><div class="avatar" style="background:#a99fd6" role="img" aria-label="Customer portrait"></div><div><div class="name">John Doe</div><div class="role">CEO, Company</div></div></div></div>
<div class="abs" style="left:574px;top:3870px;width:7px;height:7px;border-radius:50%;background:#b5a7e8"></div>
<div class="abs" style="left:597px;top:3870px;width:7px;height:7px;border-radius:50%;background:#b5a7e8"></div>
<div class="abs" style="left:620px;top:3870px;width:7px;height:7px;border-radius:50%;background:#fff"></div>

<!-- CONTACT -->
<h2 class="abs" style="left:219px;top:4030px;font-size:28px;font-weight:600;line-height:34px">LET US HEAR<br>YOUR THOUGHTS</h2>
<p class="abs" style="left:219px;top:4106px;width:290px;font-family:Roboto,sans-serif;font-size:15px;line-height:20px;color:#555">Lorem Ipsum is simply dummy text of the printing</p>
<div class="contact-line" style="top:4160px;align-items:flex-start;font-size:12.5px;line-height:16px"><svg width="14" height="18" viewBox="0 0 14 18"><path d="M7 1a6 6 0 016 6c0 4.5-6 10-6 10S1 11.5 1 7a6 6 0 016-6z" fill="var(--purple)"/><circle cx="7" cy="7" r="2.2" fill="#fff"/></svg><span>214 Elm Row #5B<br>Austin 70100 TX</span></div>
<div class="contact-line" style="top:4212px"><svg width="16" height="16" viewBox="0 0 16 16"><path d="M3 1l3 3-1.5 2.5a9 9 0 005 5L12 10l3 3-2 2C7 15 1 9 1 3z" fill="var(--purple)"/></svg><span>(555) 014 7720</span></div>
<div class="contact-line" style="top:4247px"><svg width="16" height="12" viewBox="0 0 16 12"><rect width="16" height="12" rx="1" fill="var(--purple)"/><path d="M1 1l7 6 7-6" stroke="#fff" stroke-width="1.3" fill="none"/></svg><span>hello@renewhub.net</span></div>
<div class="abs" role="img" aria-label="Street map showing the office location" style="left:625px;top:4008px;width:367px;height:270px;border-radius:3px;background:linear-gradient(135deg,#efeae0,#e6e2d6 60%,#dfe8d6)"></div>

<!-- FOOTER -->
<footer class="footer">
  <div class="abs" style="left:158px;top:52px;font-size:22px;font-weight:600">Free Monthly Newsletter</div>
  <div class="abs" style="left:158px;top:86px;font-family:Roboto,sans-serif;font-size:12px;color:#ccc">Subscribe to our newsletter for all the latest news and cool tips</div>
  <div class="abs" style="left:638px;top:61px;width:290px;height:35px;background:#fff;border-radius:18px 0 0 18px;padding:9px 24px;font-family:Roboto,sans-serif;font-size:13px;color:#999">Email address</div>
  <div class="abs" style="left:919px;top:61px;width:119px;height:35px;background:var(--purple);border-radius:0 18px 18px 0;display:flex;align-items:center;justify-content:center;font-size:14px;font-weight:500">Subscribe</div>
  <div class="logo" style="left:162px;top:166px;font-size:40px">LOGO</div>
  <p class="abs" style="left:162px;top:228px;width:180px;font-family:Roboto,sans-serif;font-size:12px;line-height:20px;color:#ddd">Lorem Ipsum is simply dummy text of the printing and typesetting industry. Lorem Ipsum has been the industry's standard dummy</p>
  <div class="fcol plain" style="left:493px"><a>HOME</a><a>NEWS</a><a>ABOUT US</a><a>CONTACT</a></div>
  <div class="fcol" style="left:677px"><h6>SERVICES</h6><a>Smartphones</a><a>Laptops</a><a>Tablets</a><a>Gadgets</a></div>
  <div class="fcol" style="left:874px"><h6>QUICK LINKS</h6><a>FAQ</a><a>Testimonials</a><a>Sitemap</a></div>
  <div class="abs" style="left:80px;top:399px;width:1120px;height:1px;background:#555"></div>
  <div class="abs" style="left:0;width:1200px;text-align:center;top:425px;font-family:Roboto,sans-serif;font-size:12px;color:#bbb">© 2020 Company Name. All Rights are Reserved.</div>
</footer>
<div class="social" style="left:547px"></div>
<div class="social" style="left:584px"></div>
<div class="social" style="left:621px"></div>
<div class="social" style="left:658px"></div>

</body>
</html>
```